Luxury Lifestyle Website - Blog and Product Showcasing

I am looking to create a simple, yet elegant website where I can post blog posts and feature products and brand partnerships for my company, Velour Hollis. I want a very elegant but not overly complex site. I like the look and feel of Harriet Osborne's site - I don't need for it to be that robust or sophisticated, but that is the aesthetic I am going for. I would like to include my primary logo at the top of the main page, and also incorporate my alternative logos throughout the site in strategic places.

Target Market(s)

Luxury Brands; 20s-60s year olds; women; high-end fashion and tastes

Industry/Entity Type

Luxury Lifestyle - Blogging - Product Showcasing

Coding

Coded - Design and coding required

Number of Pages Required

4 page

Font styles to use
Sans Serif
Script
Other font styles liked:
• Pinyon

Colors
00AB8E
00BBA5
67D7C9
C6EFE9
E9F9F6
59FF00
82FF00
B8FF75
E3FFCB
F4FFEA

Requirements
Must have
• Creative use of my various logos. PASTEL GREENS or a DEEP DARK GREEN. Nothing bright, very soft and elegant.
Nice to have
• Elegant script that is easy to read.
Should not have
• Bright colors or overly modern look or feel.

```html
<!DOCTYPE html>
<html lang="en">
<head>
<meta charset="utf-8">
<title>Velour Hollis — Luxury Lifestyle</title>
<link rel="stylesheet" href="https://fonts.googleapis.com/css2?family=Pinyon+Script&family=Roboto:wght@400;500;700&display=swap">
<style>
:root{
  --teal:#00ab8e;
  --teal-2:#00bba5;
  --mint:#cdeee6;
  --mint-soft:#e9f9f6;
  --cream:#f6f4ef;
  --ink:#1f1f1f;
  --muted:#666;
  --white:#fff;
}
*{box-sizing:border-box;margin:0;padding:0}
html,body{width:1200px;height:4584px;overflow:hidden}
body{position:relative;background:var(--cream);font-family:'Roboto',sans-serif;color:var(--ink)}
.abs{position:absolute}
.script{font-family:'Pinyon Script',cursive;font-weight:400;color:var(--ink)}
.title{position:absolute;left:0;width:1200px;text-align:center;font-size:44px;line-height:1}
.btn{position:absolute;background:var(--teal);color:var(--white);border-radius:22px;font-weight:700;font-size:13px;text-transform:uppercase;display:flex;align-items:center;justify-content:center;gap:7px;letter-spacing:.2px}
.btn .dot{width:12px;height:12px;border-radius:50%;background:var(--white);position:relative}
.btn .dot::after{content:"";position:absolute;left:4px;top:3px;border-left:5px solid var(--teal);border-top:3px solid transparent;border-bottom:3px solid transparent}
.ph{position:absolute}
.social{position:absolute;width:40px;height:40px;border-radius:50%;background:var(--teal)}
/* header */
.topbar{position:absolute;left:0;top:0;width:1200px;height:66px;background:var(--cream)}
.call-label{left:192px;top:14px;font-size:12px;color:var(--ink)}
.call-number{left:192px;top:30px;font-size:21px;font-weight:700}
.hero{position:absolute;left:0;top:66px;width:1200px;height:630px;background:linear-gradient(100deg,#5c4636 0%,#8a6d55 35%,#b9a089 60%,#a89079 100%)}
.nav{position:absolute;top:84px;font-size:12.5px;font-weight:700;color:var(--white);display:flex;gap:18px;text-transform:uppercase}
.nav-active::after{content:"";display:block;width:30px;height:3px;border-radius:2px;background:var(--teal);margin:7px auto 0}
.brand-badge{position:absolute;left:538px;top:8px;width:124px;height:124px;border-radius:50%;background:var(--white);display:flex;align-items:center;justify-content:center;text-align:center;font-size:15px;font-weight:500;color:var(--teal);line-height:1.2}
.hero-heading{left:142px;top:246px;font-size:46px;line-height:50px;color:var(--white)}
/* about */
.about-photo{left:193px;top:718px;width:356px;height:356px;border-radius:50%;border:3px solid var(--teal);background:linear-gradient(160deg,#7a5a3e,#c9a57e 55%,#2c2a3a)}
.about-title{left:600px;top:748px;font-size:46px}
.about-text{left:600px;width:442px;font-size:12.5px;line-height:21px;color:var(--muted)}
/* dress edit */
.band{position:absolute;left:0;width:1200px;background:var(--mint)}
.card{position:absolute;background:var(--white);border-radius:10px;box-shadow:0 6px 18px rgba(0,0,0,.18);text-align:center}
.card-img{position:absolute;left:8px;top:6px;right:8px;height:198px}
.card h3{position:absolute;left:0;width:100%;top:248px;font-size:16px;font-weight:500;text-transform:uppercase}
.card p{position:absolute;left:20px;right:20px;top:280px;font-size:12px;line-height:21px;color:var(--muted)}
/* shop */
.product{position:absolute;top:1998px;width:219px}
.product-img{width:219px;height:216px;background:var(--white);border:1px solid #e6e3dc;display:flex;align-items:center;justify-content:center}
.product-name{margin-top:34px;font-size:16px;font-weight:500}
.product-price{margin-top:7px;font-size:13px;color:#444}
/* video */
.video{left:283px;top:2476px;width:693px;height:359px;border-radius:8px;background:linear-gradient(120deg,#c8c4bd,#9c978e 40%,#6a6258 70%,#d8d2c6);box-shadow:0 8px 20px rgba(0,0,0,.25);overflow:hidden}
/* gallery */
.ig{position:absolute}
/* contact */
.info-label{font-size:14px;font-weight:700;text-transform:uppercase}
.info-value{font-size:12.5px;color:var(--muted);line-height:18px;margin-top:6px}
.field{position:absolute;background:var(--white);border:1px solid #e4e4e4;font-size:12px;color:#999;padding:0 18px;display:flex;align-items:center}
/* footer */
.foot-h{font-size:16px;font-weight:500}
.foot-list{list-style:none;margin-top:16px;font-size:12.5px;color:var(--muted)}
.foot-list li{margin-bottom:14px;padding-left:18px;position:relative}
.foot-list li::before{content:"»";position:absolute;left:0;color:var(--teal)}
.copyright{left:0;width:1200px;top:4533px;text-align:center;font-size:12.5px;color:var(--muted)}
</style>
</head>
<body>

<!-- header -->
<div class="topbar"></div>
<svg class="abs" style="left:142px;top:16px" width="36" height="36" viewBox="0 0 24 24" aria-hidden="true"><path fill="#00ab8e" d="M6.6 10.8a15.2 15.2 0 0 0 6.6 6.6l2.2-2.2c.3-.3.7-.4 1-.2 1.1.4 2.3.6 3.6.6.6 0 1 .4 1 1V20c0 .6-.4 1-1 1A17 17 0 0 1 3 4c0-.6.4-1 1-1h3.5c.6 0 1 .4 1 1 0 1.3.2 2.5.6 3.6.1.3 0 .7-.2 1z"/></svg>
<div class="abs call-label">Call Us Now:</div>
<div class="abs call-number">+1 555-014-2278</div>
<div class="btn" style="left:752px;top:13px;width:142px;height:40px;font-size:12.5px">Book Now</div>
<div class="social" style="left:922px;top:13px"></div>
<div class="social" style="left:968px;top:13px"></div>
<div class="social" style="left:1014px;top:13px"></div>

<!-- hero -->
<div class="hero" role="img" aria-label="Photo of a woman in an olive dress holding a woven straw bag beside stone columns"></div>
<nav class="nav" style="left:142px"><span>Home</span><span>About Us</span><span class="nav-active">Dressing Room</span><span>Home &amp; Garden</span></nav>
<nav class="nav" style="left:721px"><span>Lifestyle</span><span>Shop</span><span>Outfits</span><span>Videos</span><span>Contact</span></nav>
<div class="brand-badge">Velour<br>Hollis</div>
<h1 class="abs script hero-heading">The Authority on Living an<br>Elegantly Extravagant Existence</h1>
<div class="btn" style="left:142px;top:391px;width:190px;height:42px">Get Started <span class="dot"></span></div>
<svg class="abs" style="left:0;top:590px" width="1200" height="130" viewBox="0 0 1200 130" preserveAspectRatio="none" aria-hidden="true">
  <path fill="#f6f4ef" d="M0 105 C180 40 380 30 560 58 C760 92 940 108 1200 50 L1200 130 L0 130 Z"/>
  <path fill="#00ab8e" d="M0 92 C180 20 380 15 560 44 C760 78 940 92 1200 32 L1200 46 C940 104 760 90 560 58 C380 30 180 36 0 108 Z"/>
</svg>

<!-- about -->
<div class="abs about-photo" role="img" aria-label="Photo of a woman in a dark sequined dress among dried pampas plants"></div>
<h2 class="abs script about-title">About Us</h2>
<svg class="abs" style="left:662px;top:795px" width="40" height="8" viewBox="0 0 40 8" aria-hidden="true"><path d="M2 2 Q20 10 38 2" stroke="#00ab8e" stroke-width="2" fill="none"/></svg>
<p class="abs about-text" style="top:815px">Lorem ipsum dolor sit amet, consectetur adipiscing elit, sed do eiusmod tempor incididunt ut labore et dolore magna aliqua. Ut enim ad minim veniam, quis nostrud exercitation ullamco laboris nisi ut aliquip ex ea commodo consequat ullamco laboris nisi .</p>
<p class="abs about-text" style="top:912px">Duis aute irure dolor in reprehenderit in voluptate velit esse cillum dolore eu fugiat nulla pariatur. Excepteur sint occaecat cupidatat non proident, sunt in culpa qui officia deserunt mollit anim id est laborum.</p>
<div class="btn" style="left:600px;top:1002px;width:141px;height:40px;text-transform:none;font-size:14px">Learn More <span class="dot"></span></div>

<!-- dress edit -->
<section class="band" style="top:1158px;height:682px"></section>
<h2 class="script title" style="top:1238px">My White Dress Edit For Summer</h2>
<svg class="abs" style="left:580px;top:1283px" width="40" height="8" viewBox="0 0 40 8" aria-hidden="true"><path d="M2 2 Q20 10 38 2" stroke="#00ab8e" stroke-width="2" fill="none"/></svg>

<article class="card" style="left:142px;top:1327px;width:291px;height:415px">
  <div class="card-img" style="background:linear-gradient(135deg,#5a2a22,#b8362c 55%,#d9c6bb)" role="img" aria-label="Photo of a woman in a red dress seated by a window with flowers"></div>
  <h3>In The Dressing Room</h3>
  <p>Lorem ipsum dolor sit amet, consectetur adipiscing elit, sed do eiusmod tempor incididunt ut labore et dolore magna aliqua.</p>
  <div class="btn" style="left:72px;top:350px;width:146px;height:38px">Read More <span class="dot"></span></div>
</article>
<article class="card" style="left:458px;top:1344px;width:286px;height:415px">
  <div class="card-img" style="top:14px;background:linear-gradient(160deg,#7fa67a,#3f6a5c 50%,#222)" role="img" aria-label="Photo of a woman in a black dress by a lakeside garden"></div>
  <h3 style="top:246px">In The Home &amp; Garden</h3>
  <p>Lorem ipsum dolor sit amet, consectetur adipiscing elit, sed do eiusmod tempor incididunt ut labore et dolore magna aliqua.</p>
  <div class="btn" style="left:70px;top:358px;width:146px;height:38px">Read More <span class="dot"></span></div>
</article>
<article class="card" style="left:768px;top:1327px;width:288px;height:415px">
  <div class="card-img" style="background:linear-gradient(140deg,#e8ded6,#b9a89a 50%,#6d5a50)" role="img" aria-label="Photo of a woman in sunglasses at the wheel of a car"></div>
  <h3>Lifestyle</h3>
  <p>Lorem ipsum dolor sit amet, consectetur adipiscing elit, sed do eiusmod tempor incididunt ut labore et dolore magna aliqua.</p>
  <div class="btn" style="left:71px;top:350px;width:146px;height:38px">Read More <span class="dot"></span></div>
</article>

<!-- shop -->
<h2 class="script title" style="top:1910px">Shop</h2>
<svg class="abs" style="left:580px;top:1956px" width="40" height="8" viewBox="0 0 40 8" aria-hidden="true"><path d="M2 2 Q20 10 38 2" stroke="#00ab8e" stroke-width="2" fill="none"/></svg>
<div class="product" style="left:142px"><div class="product-img"><div class="ph" style="position:static;width:120px;height:90px;background:linear-gradient(135deg,#2a3f9a,#1b2a6b)" role="img" aria-label="Product photo of a blue high heel shoe"></div></div><div class="product-name">Product Name 1</div><div class="product-price">$20.00</div></div>
<div class="product" style="left:374px"><div class="product-img"><div class="ph" style="position:static;width:120px;height:110px;background:linear-gradient(135deg,#f1dcc0,#d9b991)" role="img" aria-label="Product photo of a beige quilted handbag with chain strap"></div></div><div class="product-name">Product Name 2</div><div class="product-price">$20.00</div></div>
<div class="product" style="left:606px"><div class="product-img"><div class="ph" style="position:static;width:90px;height:150px;background:linear-gradient(180deg,#2f4a78,#1e335a)" role="img" aria-label="Product photo of a navy sleeveless dress"></div></div><div class="product-name">Product Name 3</div><div class="product-price">$20.00</div></div>
<div class="product" style="left:837px"><div class="product-img"><div class="ph" style="position:static;width:130px;height:130px;background:linear-gradient(135deg,#e3c8b4,#a86a5a 50%,#3a3030)" role="img" aria-label="Product photo of an assortment of makeup palettes and brushes"></div></div><div class="product-name">Product Name 4</div><div class="product-price">$20.00</div></div>

<!-- video -->
<section class="band" style="top:2363px;height:344px"></section>
<h2 class="script title" style="top:2394px">Our Video</h2>
<svg class="abs" style="left:580px;top:2440px" width="40" height="8" viewBox="0 0 40 8" aria-hidden="true"><path d="M2 2 Q20 10 38 2" stroke="#00ab8e" stroke-width="2" fill="none"/></svg>
<div class="abs video" role="img" aria-label="Video still of a woman in white sunglasses and a white blazer on a city street">
  <svg class="abs" style="left:321px;top:161px" width="50" height="50" viewBox="0 0 50 50" aria-hidden="true"><circle cx="25" cy="25" r="23" fill="#00ab8e"/><circle cx="25" cy="25" r="14" fill="#fff"/><path d="M21 18 L32 25 L21 32 Z" fill="#00ab8e"/></svg>
  <div class="abs" style="left:30px;top:322px;width:633px;height:26px;background:rgba(0,0,0,.75);border-radius:3px"></div>
  <svg class="abs" style="left:52px;top:328px" width="14" height="14" viewBox="0 0 14 14" aria-hidden="true"><path d="M2 1 L13 7 L2 13 Z" fill="#fff"/></svg>
  <div class="abs" style="left:90px;top:334px;width:500px;height:3px;background:#777"></div>
  <div class="abs" style="left:90px;top:334px;width:30px;height:3px;background:#fff"></div>
  <div class="abs" style="left:600px;top:329px;width:50px;height:12px;background:rgba(255,255,255,.5);border-radius:2px"></div>
</div>

<!-- gallery -->
<h2 class="script title" style="top:2913px">Follows @ Our Journal</h2>
<svg class="abs" style="left:580px;top:2958px" width="40" height="8" viewBox="0 0 40 8" aria-hidden="true"><path d="M2 2 Q20 10 38 2" stroke="#00ab8e" stroke-width="2" fill="none"/></svg>
<div class="ig" style="left:142px;top:2992px;width:453px;height:264px;background:linear-gradient(120deg,#d9c98a,#8b6a3a 50%,#b34b2c)" role="img" aria-label="Photo of a woman in a wide black hat and red polka-dot blouse"></div>
<div class="ig" style="left:604px;top:2992px;width:452px;height:264px;background:linear-gradient(120deg,#c8a892,#b08c76 50%,#2a2222)" role="img" aria-label="Photo of a woman seated on the floor in a black blazer and cream skirt"></div>
<div class="ig" style="left:148px;top:3265px;width:299px;height:236px;background:linear-gradient(140deg,#3a2a22,#8a6a52 50%,#d8b8a2)" role="img" aria-label="Photo of a woman in a blush dress on a tufted armchair"></div>
<div class="ig" style="left:458px;top:3265px;width:290px;height:236px;background:#1aa58c" role="img" aria-label="Gallery photo behind a teal hover overlay">
  <svg class="abs" style="left:130px;top:103px" width="30" height="30" viewBox="0 0 24 24" aria-hidden="true"><circle cx="10" cy="10" r="7" stroke="#fff" stroke-width="2" fill="none"/><path d="M15 15 L21 21 M10 7 V13 M7 10 H13" stroke="#fff" stroke-width="2"/></svg>
</div>
<div class="ig" style="left:757px;top:3265px;width:299px;height:236px;background:linear-gradient(140deg,#2a2424,#5a3a30 50%,#1a1616)" role="img" aria-label="Portrait photo of a woman with red lips and long brown hair"></div>

<!-- contact -->
<section class="band" style="top:3580px;height:570px"></section>
<h2 class="script title" style="top:3607px">Contact Us</h2>
<svg class="abs" style="left:580px;top:3653px" width="40" height="8" viewBox="0 0 40 8" aria-hidden="true"><path d="M2 2 Q20 10 38 2" stroke="#00ab8e" stroke-width="2" fill="none"/></svg>

<svg class="abs" style="left:214px;top:3717px" width="48" height="48" viewBox="0 0 48 48" aria-hidden="true"><path d="M24 4a12 12 0 0 0-12 12c0 9 12 22 12 22s12-13 12-22A12 12 0 0 0 24 4z" fill="none" stroke="#00ab8e" stroke-width="2.5"/><circle cx="24" cy="16" r="4.5" fill="none" stroke="#00ab8e" stroke-width="2.5"/><path d="M4 44 L12 32 H36 L44 44 Z" fill="none" stroke="#00ab8e" stroke-width="2.5"/></svg>
<div class="abs" style="left:282px;top:3712px;width:220px"><div class="info-label">Location:</div><div class="info-value">Room 001, Lorem ipsum dolor sit amet, consectetur adipiscing</div></div>
<svg class="abs" style="left:553px;top:3717px" width="44" height="44" viewBox="0 0 24 24" aria-hidden="true"><path fill="none" stroke="#00ab8e" stroke-width="1.4" d="M6.6 10.8a15.2 15.2 0 0 0 6.6 6.6l2.2-2.2c.3-.3.7-.4 1-.2 1.1.4 2.3.6 3.6.6.6 0 1 .4 1 1V20c0 .6-.4 1-1 1A17 17 0 0 1 3 4c0-.6.4-1 1-1h3.5c.6 0 1 .4 1 1 0 1.3.2 2.5.6 3.6.1.3 0 .7-.2 1z"/></svg>
<div class="abs" style="left:620px;top:3721px"><div class="info-label">Phone:</div><div class="info-value">+1 555-014-2278</div></div>
<svg class="abs" style="left:778px;top:3723px" width="48" height="36" viewBox="0 0 48 36" aria-hidden="true"><rect x="2" y="2" width="44" height="32" fill="none" stroke="#00ab8e" stroke-width="2.5"/><path d="M2 2 L24 20 L46 2 M2 34 L18 16 M46 34 L30 16" fill="none" stroke="#00ab8e" stroke-width="2.5"/></svg>
<div class="abs" style="left:846px;top:3721px"><div class="info-label">Email:</div><div class="info-value">info@velourhollis.com</div></div>

<div class="field" style="left:185px;top:3812px;width:403px;height:46px">Name</div>
<div class="field" style="left:185px;top:3874px;width:403px;height:46px">Email Address</div>
<div class="field" style="left:185px;top:3935px;width:403px;height:46px">Phone Number</div>
<div class="field" style="left:609px;top:3811px;width:406px;height:173px;align-items:flex-start;padding-top:24px">Message</div>
<div class="btn" style="left:506px;top:4015px;width:190px;height:47px;font-size:14px">Submit Now <span class="dot"></span></div>

<svg class="abs" style="left:0;top:4100px" width="1200" height="100" viewBox="0 0 1200 100" preserveAspectRatio="none" aria-hidden="true">
  <path fill="#f6f4ef" d="M0 70 C200 100 420 80 620 40 C800 8 980 10 1200 80 L1200 100 L0 100 Z"/>
  <path fill="#00ab8e" d="M0 50 C200 86 420 68 620 30 C800 -2 980 2 1200 62 L1200 80 C980 12 800 10 620 42 C420 82 200 100 0 66 Z"/>
</svg>

<!-- footer -->
<div class="abs" style="left:142px;top:4285px;width:132px;height:132px;border-radius:50%;border:2px solid #b9b9b9;background:var(--white);display:flex;align-items:center;justify-content:center;text-align:center;font-size:16px;font-weight:500;color:var(--teal);line-height:1.2">Velour<br>Hollis</div>
<div class="social" style="left:142px;top:4426px;width:32px;height:32px;background:#e2ded6"></div>
<div class="social" style="left:181px;top:4426px;width:32px;height:32px;background:#e2ded6"></div>
<div class="social" style="left:220px;top:4426px;width:32px;height:32px"></div>
<div class="social" style="left:262px;top:4426px;width:32px;height:32px;background:#e2ded6"></div>

<div class="abs" style="left:372px;top:4292px"><div class="foot-h">Quick Links</div>
<ul class="foot-list"><li>Home</li><li>About Us</li><li>Shop</li><li>Videos</li><li>Contact Us</li></ul></div>
<div class="abs" style="left:563px;top:4292px"><div class="foot-h">Important</div>
<ul class="foot-list"><li>Terms of Use</li><li>Site Map</li><li>Privacy Policy</li><li>Disclaimer</li></ul></div>
<div class="abs" style="left:730px;top:4292px;width:240px"><div class="foot-h">Contact us</div>
  <div style="margin-top:24px;font-size:12.5px;color:var(--muted);line-height:18px;padding-left:26px;position:relative"><svg style="position:absolute;left:4px;top:2px" width="10" height="14" viewBox="0 0 10 14" aria-hidden="true"><path d="M5 0a5 5 0 0 0-5 5c0 4 5 9 5 9s5-5 5-9a5 5 0 0 0-5-5z" fill="#00ab8e"/></svg>Room 001, Lorem ipsum dolor sit amet, consectetur adipiscing</div>
  <div style="margin-top:14px;font-size:12.5px;color:var(--muted);padding-left:26px;position:relative"><svg style="position:absolute;left:4px;top:1px" width="9" height="14" viewBox="0 0 9 14" aria-hidden="true"><rect x="1" y="1" width="7" height="12" rx="1" fill="none" stroke="#00ab8e" stroke-width="1.5"/></svg>+1 555-014-2278</div>
  <div style="margin-top:14px;font-size:12.5px;color:var(--muted);padding-left:26px;position:relative"><svg style="position:absolute;left:2px;top:2px" width="13" height="10" viewBox="0 0 13 10" aria-hidden="true"><rect x="1" y="1" width="11" height="8" fill="none" stroke="#00ab8e" stroke-width="1.3"/><path d="M1 1 L6.5 5.5 L12 1" fill="none" stroke="#00ab8e" stroke-width="1.3"/></svg>info@velourhollis.com</div>
</div>
<svg class="abs" style="left:1056px;top:4480px" width="34" height="34" viewBox="0 0 34 34" aria-hidden="true"><circle cx="17" cy="17" r="16" fill="#00ab8e"/><path d="M9 11 H25 V21 H15 L11 25 V21 H9 Z" fill="#fff"/></svg>
<div class="abs copyright">Copy right © 2023 <span style="color:var(--teal)">Velour Hollis</span> | All Rights Reserved</div>

</body>
</html>
```